Business Card Design Project

Hi
I'm currently getting a logo designed which will go on the front. It is designed for s
Fitness instructor/ personal training business.
On the back I would like written:
Boxing for Fitness
Aqua Fitness Professional
PersonalisedTraining 1/1 or Small Group outdoor training
Fun and unique workouts
Weight loss/ Strength training

Also I need on there my details
minawestlake27@quellmail.net
0438 917 355
FB Mina Fitness

Reason: I would like to extend the deadline to give extra days after I have confirmed the logo in two days

Target Market(s)

Mostly women aged between 20-50

Industry/Entity Type

Training

Font styles to use
Sans Serif

Requirements
Must have
• My logo ( I have attached my favourite logo options )
My details

```html
<!DOCTYPE html>
<html lang="en">
<head>
<meta charset="utf-8">
<title>Mina Fitness – Business Card</title>
<link href="https://fonts.googleapis.com/css2?family=Open+Sans:wght@400;600&display=swap" rel="stylesheet">
<style>
  :root {
    --backdrop: #e8e8e5;
    --frame: #2e2f31;
    --paper: #ffffff;
    --brand-green: #7ac143;
    --ink: #2b2b2b;
    --ink-soft: #444444;
  }
  * { box-sizing: border-box; margin: 0; padding: 0; }
  html, body {
    width: 1200px;
    height: 828px;
    overflow: hidden;
    background: var(--backdrop);
    font-family: "Open Sans", Arial, sans-serif;
    color: var(--ink);
  }
  .sheet {
    width: 1200px;
    height: 828px;
    display: flex;
    align-items: center;
    justify-content: center;
    gap: 40px;
  }
  .card {
    position: relative;
    width: 560px;
    height: 320px;
    background: var(--frame);
    padding: 7px;
    box-shadow: 0 6px 18px rgba(0,0,0,0.18);
  }
  .card__face {
    position: relative;
    width: 100%;
    height: 100%;
    background: var(--paper);
    overflow: hidden;
  }
  .card__corner {
    position: absolute;
    top: 0;
    right: 0;
    width: 120px;
    height: 40px;
  }

  /* Brand wordmark */
  .brand {
    display: flex;
    align-items: center;
    gap: 10px;
  }
  .brand__dot {
    width: 34px;
    height: 34px;
    border-radius: 50%;
    background: var(--brand-green);
  }
  .brand__name {
    font-weight: 600;
    font-size: 34px;
    color: var(--brand-green);
    letter-spacing: 0.5px;
  }

  /* Back side */
  .card--back .brand {
    justify-content: center;
    margin-top: 56px;
  }
  .services {
    list-style: none;
    margin-top: 18px;
    text-align: center;
    font-size: 14px;
    line-height: 22px;
    color: var(--ink-soft);
  }

  /* Front side */
  .card--front .brand {
    position: absolute;
    left: 34px;
    top: 78px;
  }
  .person {
    position: absolute;
    right: 36px;
    top: 40px;
    text-align: right;
  }
  .person__name {
    font-size: 21px;
    font-weight: 400;
    letter-spacing: 0.5px;
    color: var(--ink);
  }
  .person__role {
    font-size: 10px;
    font-weight: 600;
    color: var(--ink-soft);
  }
  .contact {
    position: absolute;
    list-style: none;
    font-size: 14px;
    line-height: 22px;
    color: var(--ink);
  }
  .contact--place { left: 34px; bottom: 34px; }
  .contact--reach { right: 30px; bottom: 96px; }
  .contact li {
    display: flex;
    align-items: flex-start;
    gap: 8px;
  }
  .contact .icon {
    flex: none;
    width: 14px;
    height: 14px;
    margin-top: 4px;
    fill: var(--ink);
  }
</style>
</head>
<body>
<main class="sheet">

  <section class="card card--back" aria-label="Card back">
    <div class="card__face">
      <svg class="card__corner" viewBox="0 0 120 40" aria-hidden="true">
        <polygon points="0,0 120,0 120,40" fill="var(--brand-green)"/>
      </svg>
      <div class="brand">
        <span class="brand__dot"></span>
        <span class="brand__name">Mina Fitness</span>
      </div>
      <ul class="services">
        <li>Boxing for Fitness</li>
        <li>Fun and unique workouts</li>
        <li>Aqua Fitness Professional</li>
        <li>Weight loss/ Strength training</li>
        <li>Personalised Training 1/1 or Small Group outdoor training</li>
      </ul>
    </div>
  </section>

  <section class="card card--front" aria-label="Card front">
    <div class="card__face">
      <svg class="card__corner" viewBox="0 0 120 40" aria-hidden="true">
        <polygon points="0,0 120,0 120,40" fill="var(--brand-green)"/>
      </svg>

      <div class="person">
        <p class="person__name">DANA PRUITT</p>
        <p class="person__role">Graphics Designer</p>
      </div>

      <div class="brand">
        <span class="brand__dot"></span>
        <span class="brand__name">Mina Fitness</span>
      </div>

      <ul class="contact contact--reach">
        <li>
          <svg class="icon" viewBox="0 0 14 14" aria-hidden="true">
            <path d="M1 3h12v8H1z" fill="none" stroke="var(--ink)" stroke-width="1.4"/>
            <path d="M1 3l6 5 6-5" fill="none" stroke="var(--ink)" stroke-width="1.4"/>
          </svg>
          <span>minawestlake27@quellmail.net</span>
        </li>
        <li>
          <svg class="icon" viewBox="0 0 14 14" aria-hidden="true">
            <rect x="3.5" y="0.5" width="7" height="13" rx="1.2" fill="none" stroke="var(--ink)" stroke-width="1.3"/>
            <rect x="5.5" y="11" width="3" height="1"/>
          </svg>
          <span>0438 917 355</span>
        </li>
        <li>
          <svg class="icon" viewBox="0 0 14 14" aria-hidden="true">
            <rect x="1" y="1" width="12" height="12" rx="2"/>
          </svg>
          <span>FB Mina Fitness</span>
        </li>
      </ul>

      <ul class="contact contact--place">
        <li>
          <svg class="icon" viewBox="0 0 14 14" aria-hidden="true">
            <path d="M7 1L0.5 7H2.5v6h3.5V9h2v4h3.5V7h2z"/>
          </svg>
          <span>4820 Alder Reach Ct Harlow<br>NY D0573</span>
        </li>
        <li>
          <svg class="icon" viewBox="0 0 14 14" aria-hidden="true">
            <circle cx="7" cy="7" r="6" fill="none" stroke="var(--ink)" stroke-width="1.3"/>
            <ellipse cx="7" cy="7" rx="2.6" ry="6" fill="none" stroke="var(--ink)" stroke-width="1.1"/>
            <path d="M1 7h12M2 4h10M2 10h10" fill="none" stroke="var(--ink)" stroke-width="1"/>
          </svg>
          <span>www.minafitstudio.net</span>
        </li>
      </ul>
    </div>
  </section>

</main>
</body>
</html>
```